Brinewardsea.com Website design needed!!

We are looking for a website layout to match the attached logo. We specialize in Dive Charters and currently are located in the Virgin Islands off of St. Thomas. Please create a design that is compatible with Bootstrap and have the grid in mind. WE are looking for creative and extremely professional layout design.

Target Market(s)

Scuba Diving, Divers looking for a diving charter in the Virgin Islands.

Number of Pages Required

3 page

Font styles to use
Serif

Requirements
Must have
• Must be Bootstrap friendly.
• Must work with the logo we provided. Colors etc.

```html
<!DOCTYPE html>
<html lang="en">
<head>
<meta charset="utf-8">
<title>Brinewardsea — Dive Charters</title>
<link rel="stylesheet" href="https://fonts.googleapis.com/css2?family=Mulish:wght@400;500&display=swap">
<style>
:root{
  --navy:#25235f;
  --navy-deep:#262466;
  --sky-top:#eef7fd;
  --sky-mid:#3a9ad8;
  --brand-red:#e8202a;
  --ink:#1f2a6b;
  --white:#ffffff;
  --social:#3b63b0;
}
*{box-sizing:border-box;margin:0;padding:0}
html,body{width:1200px;height:1200px;overflow:hidden;background:var(--white);font-family:"Mulish",sans-serif;color:var(--navy)}
.page{position:relative;width:1200px;height:1200px}
.hero{position:absolute;left:0;top:0;width:1200px;height:400px;
  background:linear-gradient(180deg,var(--sky-top) 0%,#cfe8f8 12%,#8cc8ef 20%,var(--sky-mid) 40%,#2a63b0 70%,var(--navy-deep) 100%)}
.hero-rule{position:absolute;left:0;top:101px;width:1200px;height:1px;background:rgba(58,154,216,.35)}
.brand{position:absolute;left:222px;top:38px;display:flex;align-items:center;gap:10px;font-size:30px;font-weight:500;color:var(--brand-red)}
.brand-dot{width:26px;height:26px;border-radius:50%;background:var(--brand-red)}
.social{position:absolute;top:4px;left:834px;display:flex;gap:9px}
.social span{width:22px;height:22px;border-radius:50%;background:var(--social)}
.social span.red{background:#d6342a}
.social span.light{background:#6f8fb8}
.phone{position:absolute;top:38px;right:216px;display:flex;align-items:center;gap:6px;font-size:11px;color:var(--navy)}
.nav{position:absolute;top:62px;left:466px;display:flex;gap:25px;font-size:19px;color:var(--ink)}
.nav a{color:inherit;text-decoration:none;padding-bottom:9px;border-bottom:2px solid transparent}
.nav a.active{border-bottom-color:var(--ink)}
.nav a.hover{border-bottom-color:var(--sky-mid)}
.search-title{position:absolute;top:126px;width:1200px;text-align:center;font-size:24px;color:var(--white)}
.choice{position:absolute;top:181px;display:flex;align-items:center;gap:11px;font-size:15px;color:var(--white)}
.choice i{display:block;width:21px;height:21px;border-radius:50%;background:var(--white)}
.field{position:absolute;top:232px;width:240px;height:40px;background:var(--white);border:1px solid #ccd;border-radius:2px;padding:10px 8px;font-size:15px;color:#9a9aa8}
.cta{position:absolute;left:484px;top:304px;width:232px;height:61px;background:var(--brand-red);display:flex;align-items:center;color:var(--white);font-size:20px}
.cta .icon{width:81px;height:61px;border-right:1px solid rgba(0,0,0,.15);display:flex;align-items:center;justify-content:center}
.cta .label{padding-left:16px}
.section-title{position:absolute;left:215px;font-size:20px;font-weight:400;color:var(--navy);text-transform:uppercase}
.photo{position:absolute}
.intro-text{position:absolute;left:681px;top:462px;width:310px;font-size:19.3px;line-height:21.9px;color:var(--navy)}
.news{position:absolute;color:var(--navy)}
.news h3{font-size:18.5px;font-weight:400;line-height:20.5px;margin-bottom:6px}
.news p{font-size:11.4px;line-height:13.5px}
.footer-rule{position:absolute;left:0;top:1156px;width:1200px;height:1px;background:#d8dbe8}
.footer{position:absolute;left:0;top:1161px;width:1200px;height:39px;background:var(--navy-deep);color:var(--white);font-size:15px;text-align:center;line-height:39px}
</style>
</head>
<body>
<div class="page">
  <header class="hero">
    <div class="hero-rule"></div>
    <div class="brand"><span class="brand-dot"></span>Brinewardsea</div>
    <div class="social" aria-label="Social links"><span></span><span class="light"></span><span class="red"></span><span class="red"></span><span class="light"></span></div>
    <div class="phone">
      <svg width="20" height="20" viewBox="0 0 20 20"><circle cx="10" cy="10" r="9" fill="none" stroke="#3a9ad8" stroke-width="1.4"/><path d="M6.5 6.5c.6-.6 1.2-.5 1.6 0l.8 1.2c.3.5.2 1-.2 1.3l-.4.3c.5 1 1.3 1.8 2.3 2.3l.3-.4c.3-.4.8-.5 1.3-.2l1.2.8c.5.4.6 1 0 1.6-.8.8-2 .9-3.2.2-1.6-.9-3-2.3-3.9-3.9-.7-1.2-.6-2.4.2-3.2z" fill="#3a9ad8"/></svg>
      (555)-014-2290
    </div>
    <nav class="nav">
      <a class="active">Brinewardsea</a><a>About Us</a><a>Contact</a><a>Learn More</a><a class="hover">Schedule</a>
    </nav>
    <h1 class="search-title" style="font-weight:400">Search for your dream charter TODAY!</h1>
    <label class="choice" style="left:437px"><i></i>I have approximate days</label>
    <label class="choice" style="left:659px"><i></i>I'm flexible</label>
    <div class="field" style="left:328px">First Name</div>
    <div class="field" style="left:632px">Email</div>
    <div class="cta">
      <span class="icon"><svg width="42" height="42" viewBox="0 0 42 42"><circle cx="21" cy="21" r="19" fill="none" stroke="#fff" stroke-width="2.5"/><path d="M16 11l13 10-13 10 4-10z" fill="#fff"/></svg></span>
      <span class="label">Find Charters</span>
    </div>
  </header>

  <h2 class="section-title" style="top:426px">Brinewardsea Charters and Scuba</h2>
  <div class="photo" role="img" aria-label="Scuba diver underwater with mask and regulator among bubbles"
       style="left:216px;top:462px;width:449px;height:252px;background:radial-gradient(ellipse at 55% 55%,#3b7fa8 0%,#1b6fae 45%,#0d3f78 100%)"></div>
  <p class="intro-text">Lorem ipsum dolor sit amet, consec­tetur adipiscing elit. Fusce semper vitae leo sit amet vehicula. Sed viverra, justo ac consectetur hendre­rit, lacus elit tempor urna, gravida mattis lacus ex sed sem. Nam con­sectetur, arcu in iaculis dapibus, urna felis congue elit, in consectetur nisi massa sed metus. Nullam a tortor ut mauris auctor interdum id vel neque. In commodo diam at faucibus</p>

  <h2 class="section-title" style="top:736px">Latest News</h2>

  <div class="photo" role="img" aria-label="Two divers in deep blue water" style="left:217px;top:772px;width:182px;height:176px;background:linear-gradient(180deg,#1a6fd0,#0c2f8a)"></div>
  <article class="news" style="left:404px;top:768px;width:188px">
    <h3>Phasellus vel eleifend</h3>
    <p style="padding-left:4px">A Caribbean luxury yacht charter is the most exclusive and most per­sonalized way to explore the Carib­bean. Whesether you want to lounge in a top-deck hot tub, taste fine wines from an onboard ce pre­pared by an award-winning chef, our team of dedicated professionals can help you book the Caribbean… Read more »</p>
  </article>

  <div class="photo" role="img" aria-label="Family on a sailing yacht deck at sea" style="left:604px;top:772px;width:183px;height:175px;background:linear-gradient(180deg,#dfe8f2 0%,#4f86c0 45%,#2b5e9e 75%,#c9d2dc 100%)"></div>
  <article class="news" style="left:795px;top:768px;width:192px">
    <h3>Caribbean Luxury Yacht Charter</h3>
    <p>A Caribbean luxury yacht charter is the most exclusive and most per­sonalized way to explore the Carib­bean. Whesether you want to lounge in a top-deck hot tub, taste fine wines from an onboard ce pre­pared by an award-winning chef, our team of dedicated professionals can help you book the Caribbean… Read more »</p>
  </article>

  <article class="news" style="left:215px;top:962px;width:186px">
    <h3>Aenean eu fringilla augue</h3>
    <p>A Caribbean luxury yacht charter is the most exclusive and most per­sonalized way to explore the Carib­bean. Whesether you want to lounge in a top-deck hot tub, taste fine wines from an onboard ce pre­pared by an award-winning chef, our team of dedicated professionals can help you book the Caribbean… Read more »</p>
  </article>
  <div class="photo" role="img" aria-label="Aerial view of a marina with boats" style="left:408px;top:965px;width:182px;height:175px;background:radial-gradient(ellipse at 55% 55%,#2f5a55 0%,#55664a 60%,#8a8570 100%)"></div>

  <article class="news" style="left:601px;top:964px;width:190px">
    <h3>Lorem ipsum dolor sit</h3>
    <p style="padding-left:4px">A Caribbean luxury yacht charter is the most exclusive and most per­sonalized way to explore the Carib­bean. Whesether you want to lounge in a top-deck hot tub, taste fine wines from an onboard ce pre­pared by an award-winning chef, our team of dedicated professionals can help you book the Caribbean… Read more »</p>
  </article>
  <div class="photo" role="img" aria-label="Diver beside a dark reef wall in black and white" style="left:797px;top:967px;width:183px;height:174px;background:radial-gradient(ellipse at 40% 30%,#6a6a6a 0%,#2a2a2a 60%,#0e0e0e 100%)"></div>

  <div class="footer-rule"></div>
  <footer class="footer">Copyright (c) Brinewardsea Divers 2016</footer>
</div>
</body>
</html>
```